PowerPoint Template for Regional Harmony Institute. Website is www.regionalharmonyinstitute.com

The tagline for the Center is "Connecting the brightest minds in healthcare"

```html
<!DOCTYPE html>
<html lang="en">
<head>
<meta charset="utf-8">
<title>What we do – Regional Harmony Institute</title>
<link href="https://fonts.googleapis.com/css2?family=Carlito:wght@400;700&display=swap" rel="stylesheet">
<style>
  :root {
    --brand-blue: #4472c4;
    --navy: #1f3f6e;
    --ink: #111111;
    --paper: #ffffff;
    --map-grey: #d9d9d9;
    --map-grey-dark: #bfbfbf;
    --shadow: rgba(0, 0, 0, 0.18);
  }
  * { box-sizing: border-box; margin: 0; padding: 0; }
  html, body { width: 1200px; height: 672px; overflow: hidden; background: var(--paper); }
  .slide {
    position: relative;
    width: 1200px;
    height: 672px;
    background: var(--paper);
    font-family: "Carlito", "Calibri", sans-serif;
    color: var(--ink);
    overflow: hidden;
  }
  .header-frame { position: absolute; inset: 0; pointer-events: none; }
  .brand-badge {
    position: absolute;
    left: 27px; top: 27px;
    width: 86px; height: 86px;
    border-radius: 50%;
    border: 5px solid var(--brand-blue);
    background: var(--paper);
    box-shadow: 0 3px 6px var(--shadow);
    display: flex; align-items: center; justify-content: center;
    font-size: 22px; font-weight: 700; color: var(--navy);
  }
  .slide-title {
    position: absolute;
    left: 165px; top: 44px;
    font-size: 44px; font-weight: 400; line-height: 1;
  }
  .intro {
    position: absolute;
    left: 81px; top: 210px;
    width: 540px;
    font-size: 19px; line-height: 26px;
  }
  .points { position: absolute; left: 84px; top: 318px; list-style: none; }
  .points li {
    display: flex; align-items: center;
    height: 36px;
    font-size: 19px;
  }
  .points li::before {
    content: "";
    width: 22px; height: 22px; border-radius: 50%;
    margin-right: 16px;
    background: radial-gradient(circle at 35% 30%, #ffffff 0%, #a9b6c8 45%, #4d5d75 100%);
  }
  .network-map {
    position: absolute;
    left: 640px; top: 200px;
    width: 560px; height: 315px;
    border-radius: 24px;
    background: radial-gradient(circle at 50% 50%, #b9c6d8 0%, var(--map-grey) 45%, #ececec 100%);
  }
  .page-number {
    position: absolute;
    left: 1077px; top: 568px;
    width: 88px; height: 88px;
    border-radius: 50%;
    border: 5px solid var(--brand-blue);
    display: flex; align-items: center; justify-content: center;
    font-size: 28px;
  }
</style>
</head>
<body>
<main class="slide">
  <svg class="header-frame" width="1200" height="672" viewBox="0 0 1200 672" aria-hidden="true">
    <path d="M100 44 Q112 22 140 22 L905 22 Q930 22 935 46 L938 66" fill="none" stroke="var(--brand-blue)" stroke-width="5"/>
    <g class="tool-icons">
      <g transform="translate(970 66)">
        <circle r="40" fill="var(--paper)" stroke="var(--brand-blue)" stroke-width="5"/>
        <circle r="30" fill="var(--paper)" style="filter:drop-shadow(0 2px 3px rgba(0,0,0,.25))"/>
        <path d="M-10 -18 V-2 Q-10 8 0 8 Q10 8 10 -2 V-18 M0 8 V14 Q0 22 9 22 Q16 22 16 14 V6" fill="none" stroke="var(--navy)" stroke-width="3" stroke-linecap="round"/>
        <circle cx="16" cy="3" r="4" fill="none" stroke="var(--navy)" stroke-width="3"/>
      </g>
      <g transform="translate(1057 66)">
        <circle r="40" fill="var(--paper)" stroke="var(--brand-blue)" stroke-width="5"/>
        <circle r="30" fill="var(--paper)" style="filter:drop-shadow(0 2px 3px rgba(0,0,0,.25))"/>
        <circle r="20" fill="var(--navy)"/>
        <path d="M-4 -12 H4 V-4 H12 V4 H4 V12 H-4 V4 H-12 V-4 H-4 Z" fill="var(--paper)"/>
      </g>
      <g transform="translate(1142 66)">
        <circle r="40" fill="var(--paper)" stroke="var(--brand-blue)" stroke-width="5"/>
        <circle r="30" fill="var(--paper)" style="filter:drop-shadow(0 2px 3px rgba(0,0,0,.25))"/>
        <rect x="-10" y="-18" width="20" height="26" rx="5" fill="var(--navy)"/>
        <rect x="-2" y="8" width="4" height="8" fill="var(--navy)"/>
        <path d="M0 16 V24" stroke="var(--navy)" stroke-width="2"/>
      </g>
    </g>
  </svg>

  <div class="brand-badge">RHI</div>
  <h1 class="slide-title">What we do</h1>

  <p class="intro">The Regional Harmony Institute (RHI) brings the brightest minds in healthcare to support key healthcare initiatives and address the nation's most pressing challenges through:</p>
  <ul class="points">
    <li>Identification of needed talent</li>
    <li>Initiative alignment and prioritization</li>
    <li>Connecting those with issues to those with solutions</li>
  </ul>

  <div class="network-map" role="img" aria-label="Grey map of the United States with a central hub connected by lines to healthcare icons such as a stethoscope, ambulance, lab flask, test tubes, tooth, eye, heart, factory and globe"></div>

  <div class="page-number">2</div>
</main>
</body>
</html>
```